依頼概要
いま、テクノロジーの進化や人々の価値変容なども手伝い、デバイス(機械)が人々に提供する価値そのものや、デバイスと人々の関係という側面に新たな価値が生まれています。

Kestra社のZolvoやNemu、自動車のVARNO、チャットボットやスマートスピーカー、スマートウォッチなど、さまざまなデバイス(≒サービス)が新たな価値提供をおこない、人々の評価を得るようになっています。

「パソコン」はどうでしょうか。

少しずつアップデートはしておりますが、「新しい!」「便利!」といった体験はあまり生み出されていないように感じます。

そのような中で、今回はミクロバの皆様から、国内で人気のパソコンブランドにプリインストールされるコミュニケーションツールの企画を募集いたします。

このコミュニケーションツールを通じて

A:安心感
B:利便性
C:ワクワク

を提供して、パソコンとユーザーのエンゲージメントをもっと深めていける、そんなコミュニケーションツールです。

今回は、そのコミュニケーションツールにおける、下記を募集いたします。

① 上記のA〜Cのいずれかを達成する機能
② ①をどのようにコミュニケーションするのか(UX)
③ ①の見え方(UI)

また、下記を踏まえて企画をおまとめください。

・A〜Cのすべてでも、いずれかに特化したものでも構いません
・①〜③のうち、①+②、①+③、①+②+③の組み合わせ

なお、「コミュニケーションツール」という言葉は、とても抽象的なものですが、参考事例をふたつお伝えしておきます。

●事例(1) Nemu(Kestra)
・デバイス(Lok / Zolvoなど)とユーザーをつなぐコミュニケーションツール
・利便性とワクワクを提供している
・「Hey, Nemu」と話しかけたり、キーボードのNemuボタンに触れるだけで呼び出しが可能
・指1本動かさなくても、様々なタスクを実行してくれる
・先を読んだ提案も可能

●事例(2)VARNO
・買って終わらない、機能が進化し続けるEV(電気自動車)
・自動車というより車輪を持ったスマートフォンのような在り方
・次はどのような進化をするのだろう、というワクワクを提供する

●事例(3)ルミナボード(Kestra)
・Kestra社独自のZolvo機能を使える場所
・利便性を提供している
・Zolvo画面上部から下にスワイプするだけで表示される
・ユーザーがある程度カスタマイズできる

これまでにない斬新なアイデアだけでなく、既存の機能をブラッシュアップしたものも含めて、皆様から多彩なアイデアをお待ちしております。

ユーザーの気持ちに寄り添ったものや、自身の経験(課題)を踏まえたアイデアだったため。

皆さま、ご提案ありがとうございました。頂戴したアイデアを参考に実装に向けて走り出します!

```html
<!DOCTYPE html>
<html lang="ja">
<head>
<meta charset="utf-8">
<title>情報探しのお手伝い</title>
<link href="https://fonts.googleapis.com/css2?family=Yomogi&display=swap" rel="stylesheet">
<style>
:root{
  --paper:#ffffff;
  --ink:#3a3a3a;
  --line:#8a8a8a;
  --note:#d8453a;
  --sunny:#f6d66a;
  --smile:#f2b7c6;
  --cool:#9fd8d6;
  --sigh:#c9c9c9;
  --blush:#e9535a;
}
*{box-sizing:border-box;margin:0;padding:0}
html,body{width:874px;height:1200px;overflow:hidden;background:var(--paper)}
body{font-family:"Yomogi",cursive;color:var(--ink);position:relative}
.abs{position:absolute}
.title{left:50px;top:30px;font-size:27px;letter-spacing:1px}
.subtitle{left:175px;top:72px;font-size:20px}
.note{color:var(--note);font-size:13px;line-height:1.35}
.note-top-left{left:70px;top:118px}
.note-top-right{left:760px;top:26px;width:100px;font-size:11px;color:var(--ink)}
.mood-row{left:58px;top:150px;display:flex;gap:12px}
.mood{width:170px;height:135px;border:1.5px solid var(--line);border-radius:4px;position:relative;padding:6px}
.mood .label{font-size:15px;text-align:center}
.mood .art{position:absolute;left:25px;right:25px;bottom:10px;height:78px;border-radius:10px}
.mood.sunny{background:color-mix(in srgb,var(--sunny) 35%,white)}
.mood.smile{background:color-mix(in srgb,var(--smile) 35%,white)}
.mood.cool{background:color-mix(in srgb,var(--cool) 35%,white)}
.mood.sigh{background:color-mix(in srgb,var(--sigh) 35%,white)}
.sunny .art{background:var(--sunny)} .smile .art{background:var(--smile)}
.cool .art{background:var(--cool)} .sigh .art{background:var(--sigh)}
.note-choice{left:120px;top:292px;font-size:14px}
.ask{font-size:13px;line-height:1.3}
.box{border:1.5px solid var(--line);font-size:14px;text-align:center;padding:4px 0;background:#fff}
.cat{width:150px;top:548px}
.opt{width:96px;font-size:13px;padding:3px 0}
.note-filter{left:18px;top:752px;width:190px}
.bubble{left:250px;top:790px;width:430px;height:56px;border:1.5px solid var(--line);border-radius:28px;font-size:17px;display:flex;align-items:center;justify-content:center}
.blob{width:150px;height:110px;top:1030px;border-radius:50%;filter:blur(6px)}
.result-text{left:110px;top:1068px;width:680px;display:flex;justify-content:space-around;font-size:22px;color:#555}
</style>
</head>
<body>
<svg class="abs" width="874" height="1200" style="left:0;top:0" aria-hidden="true">
  <g stroke="var(--line)" stroke-width="1.3" fill="none">
    <line x1="155" y1="415" x2="155" y2="540"/>
    <line x1="280" y1="415" x2="280" y2="540"/>
    <line x1="430" y1="415" x2="430" y2="540"/>
    <line x1="155" y1="540" x2="760" y2="540"/>
    <line x1="130" y1="572" x2="130" y2="740"/>
    <line x1="305" y1="572" x2="305" y2="760"/>
    <line x1="480" y1="572" x2="480" y2="720"/>
    <line x1="690" y1="572" x2="690" y2="720"/>
  </g>
  <path d="M200 860 C320 845 520 850 720 858" stroke="var(--blush)" stroke-width="9" fill="none" stroke-linecap="round" opacity=".8"/>
  <path d="M710 770 c-8 -12 -22 -2 -12 10 l12 12 12 -12 c10 -12 -4 -22 -12 -10z" fill="var(--blush)"/>
</svg>

<h1 class="abs title">ex. あなたの求めている情報探しのお手伝い。</h1>
<p class="abs subtitle">今日のテンションを教えてね。</p>
<p class="abs note-top-right">その日の気分で情報の色が変わり案内役も変わります</p>
<p class="abs note note-top-left">状況説明を吹き出しで入れる（ボタン式にも）</p>

<div class="abs mood-row">
  <div class="mood sunny"><p class="label">はつらつ の日</p><div class="art" role="img" aria-label="元気なキャラクターのイラスト"></div></div>
  <div class="mood smile"><p class="label">ほほえみ の日</p><div class="art" role="img" aria-label="ほほえむキャラクターのイラスト"></div></div>
  <div class="mood cool"><p class="label">クール な日</p><div class="art" role="img" aria-label="クールなキャラクターのイラスト"></div></div>
  <div class="mood sigh"><p class="label">ためいき の日</p><div class="art" role="img" aria-label="ためいきをつく動物のイラスト"></div></div>
</div>
<p class="abs note note-choice">選択したイメージカラーでゴールまで導いてくれます</p>

<p class="abs note" style="left:22px;top:345px;width:88px">気分に合わせた言葉で話しかけてくれます</p>
<p class="abs ask" style="left:115px;top:320px">どんな情報を<br>知りたいですか？</p>
<p class="abs ask" style="left:240px;top:320px">どんな情報を<br>探しますか？</p>
<p class="abs ask" style="left:380px;top:320px">どんな情報を<br>お探しですか？</p>
<p class="abs ask" style="left:560px;top:320px">比較したい情報を<br>選んでください</p>
<div class="abs" role="img" aria-label="小鳥のイラスト" style="left:690px;top:322px;width:40px;height:30px;border-radius:50%;background:#e3e3e3"></div>
<p class="abs" style="left:120px;top:365px;font-size:12px">場所</p>
<div class="abs box" style="left:115px;top:385px;width:80px">〇〇県</div>
<div class="abs box" style="left:380px;top:385px;width:100px">どこで店</div>
<div class="abs box" style="left:570px;top:385px;width:100px">口コミ評判</div>
<p class="abs" style="left:390px;top:365px;font-size:12px">情報カテゴリー</p>
<p class="abs note" style="left:660px;top:420px;width:150px;color:var(--ink)">たくさんの選択肢から気軽に選べます</p>

<div class="abs box cat" style="left:60px">利便性</div>
<div class="abs box cat" style="left:235px">利用人数</div>
<div class="abs box cat" style="left:410px;font-size:13px">ショップのこだわり</div>
<div class="abs box cat" style="left:620px">評判</div>

<div class="abs box opt" style="left:85px;top:600px">駐車場あり</div>
<div class="abs box opt" style="left:85px;top:640px">最寄り駅</div>
<div class="abs box opt" style="left:260px;top:600px">1〜2人</div>
<div class="abs box opt" style="left:260px;top:640px">3〜4人</div>
<div class="abs box opt" style="left:260px;top:680px">5〜10人</div>
<div class="abs box opt" style="left:260px;top:720px">10人以上</div>
<div class="abs box opt" style="left:435px;top:600px">自家製たれ</div>
<div class="abs box opt" style="left:435px;top:640px">品が多い</div>
<div class="abs box opt" style="left:435px;top:680px">国産素材</div>
<div class="abs box opt" style="left:645px;top:600px">☆☆☆☆以上</div>
<div class="abs box opt" style="left:645px;top:640px">☆☆☆以上</div>
<div class="abs box opt" style="left:645px;top:680px">☆☆以上</div>

<p class="abs note note-filter">この欄の内容を選ぶと、ぴったりの情報に絞り込めます</p>
<div class="abs bubble">あなたに ぴったりの情報が届きますように</div>
<div class="abs" role="img" aria-label="見守るキャラクターのイラスト" style="left:720px;top:790px;width:60px;height:60px;border-radius:50%;background:#e6e6e6"></div>

<div class="abs blob" style="left:95px;background:var(--sunny)"></div>
<div class="abs blob" style="left:275px;background:var(--smile)"></div>
<div class="abs blob" style="left:455px;background:var(--cool)"></div>
<div class="abs blob" style="left:635px;background:var(--sigh)"></div>
<p class="abs result-text"><span>そ</span><span>れ</span><span>ぞ</span><span>れ</span><span>の</span><span>情</span><span>報</span></p>
</body>
</html>
```